Business Card Design Project

We need a business card design for a new company based in New York called "Marble Fox's". We do major installations of energy saving devices primarily LED lighting in large facilities. We would like a double sided card with our contact info on one side with our logo (to be designed) and on the other side the services we provide. We would like a heavy weight glossy card using the colors green and white. The final design should communicate environmental soundness and our market is very upscale corporations.
We would like our logo to illustrate LED lighting and we were thinking if we could get a stock picture of the Corliss Vane Building lit up on July 4th with red, white and blue LED lighting. The alternative would be anything that connotes environmentally proper thinking. It could be either a picture or a design.

```html
<!DOCTYPE html>
<html lang="en">
<head>
<meta charset="utf-8">
<title>Marble Fox's – Business Card</title>
<link href="https://fonts.googleapis.com/css2?family=Comfortaa:wght@400;700&display=swap" rel="stylesheet">
<style>
  :root {
    --page-bg: #e9ebe8;
    --card-white: #ffffff;
    --card-shade: #eceeee;
    --leaf-green: #7cc242;
    --leaf-light: #a8d84a;
    --leaf-dark: #4f9a2a;
    --edge-blue: #3cbde8;
    --title-blue: #2a9fd0;
    --name-grey: #7a7a7a;
    --email-green: #2f5d14;
    --text-white: #ffffff;
  }
  * { margin: 0; padding: 0; box-sizing: border-box; }
  html, body {
    width: 1200px;
    height: 900px;
    overflow: hidden;
    background: var(--page-bg);
    font-family: "Comfortaa", sans-serif;
  }
  .canvas {
    position: relative;
    width: 1200px;
    height: 900px;
  }
  .card {
    position: absolute;
    left: 250px;
    width: 700px;
    height: 400px;
    background: radial-gradient(ellipse at 55% 40%, var(--card-white) 0%, var(--card-shade) 100%);
    box-shadow: 0 6px 18px rgba(0,0,0,0.18);
    overflow: hidden;
  }
  .card-back { top: 40px; }
  .card-front { top: 470px; }

  .brand {
    position: absolute;
    display: flex;
    align-items: center;
    gap: 14px;
  }
  .brand-dot {
    border-radius: 50%;
    background: var(--leaf-green);
  }
  .brand-name {
    font-family: "Comfortaa", sans-serif;
    font-weight: 700;
    color: var(--leaf-green);
    white-space: nowrap;
  }
  .card-back .brand {
    left: 50%;
    top: 50%;
    transform: translate(-50%, -50%);
  }
  .card-back .brand-dot { width: 64px; height: 64px; }
  .card-back .brand-name { font-size: 52px; }

  .card-front .brand {
    right: 34px;
    top: 60px;
    flex-direction: column;
    gap: 10px;
  }
  .card-front .brand-dot { width: 70px; height: 70px; }
  .card-front .brand-name { font-size: 30px; }

  .leaf-band {
    position: absolute;
    left: 0;
    top: 0;
    width: 700px;
    height: 400px;
  }
  .holder-name {
    position: absolute;
    left: 210px;
    top: 38px;
    font-size: 32px;
    font-weight: 700;
    letter-spacing: 9px;
    color: var(--name-grey);
    white-space: nowrap;
  }
  .holder-title {
    position: absolute;
    left: 290px;
    top: 84px;
    font-size: 18px;
    color: var(--title-blue);
    white-space: nowrap;
  }
  .contact {
    position: absolute;
    font-size: 21px;
    color: var(--text-white);
    white-space: nowrap;
  }
  .contact-phone { left: 88px; top: 186px; }
  .contact-cell { left: 112px; top: 218px; }
  .contact-email {
    left: 196px;
    top: 342px;
    color: var(--email-green);
  }
</style>
</head>
<body>
<main class="canvas">

  <section class="card card-back" aria-label="Card back">
    <div class="brand">
      <span class="brand-dot"></span>
      <span class="brand-name">Marble Fox's</span>
    </div>
  </section>

  <section class="card card-front" aria-label="Card front">
    <svg class="leaf-band" viewBox="0 0 700 400" role="img" aria-label="Large green leaf illustration sweeping across the card">
      <defs>
        <linearGradient id="leafFill" x1="0" y1="0" x2="1" y2="1">
          <stop offset="0" stop-color="#4f9a2a"/>
          <stop offset="0.5" stop-color="#7cc242"/>
          <stop offset="1" stop-color="#a8d84a"/>
        </linearGradient>
      </defs>
      <path d="M70,0 C140,86 212,142 322,164 C454,188 556,254 700,322 L700,400 L130,400 C50,290 30,120 70,0 Z"
            fill="#3cbde8"/>
      <path d="M80,0 C150,92 220,152 330,172 C460,196 560,262 700,332 L700,400 L140,400 C62,288 42,120 80,0 Z"
            fill="url(#leafFill)"/>
    </svg>

    <h1 class="holder-name">Dana Reyes</h1>
    <p class="holder-title">General Manager</p>

    <div class="brand">
      <span class="brand-dot"></span>
      <span class="brand-name">Marble Fox's</span>
    </div>

    <p class="contact contact-phone">Ph.555-40-218</p>
    <p class="contact contact-cell">Cell.555-40-218</p>
    <p class="contact contact-email">Email.dana@marblefoxs.com</p>
  </section>

</main>
</body>
</html>
```